Card design for orthopaedic surgeons working as The Brindlewood Orthopaedic Centre

Business cards, letterhead

Colors

Designer to choose colors to be used in the design.

Requirements
Must have
• Late addition.
• Cards letterhead must have logos of
• Corvane Federated Institute of Surgeons
• Meridale Orthopaedic Society
Nice to have
• Back of card to have space for appointment time to be added by hand and some blank space for writing incidental other notes.

```html
<!DOCTYPE html>
<html lang="en">
<head>
<meta charset="utf-8">
<title>The Brindlewood Orthopaedic Centre – Business Card</title>
<link rel="stylesheet" href="https://fonts.googleapis.com/css2?family=Open+Sans:wght@300;400;600;700&display=swap">
<style>
  :root {
    --backdrop: #2a2a2c;
    --card-white: #ffffff;
    --card-navy: #032c47;
    --accent-blue: #2aa6e8;
    --ink-navy: #0b2a45;
    --ink-grey: #555a5f;
    --rule-grey: #9a9a9a;
  }
  * { margin: 0; padding: 0; box-sizing: border-box; }
  html, body {
    width: 1200px; height: 960px; overflow: hidden;
    background: var(--backdrop);
    font-family: "Open Sans", Arial, sans-serif;
  }
  .canvas { position: relative; width: 1200px; height: 960px; }
  .card {
    position: absolute; left: 261px; width: 679px; height: 387px;
    border-radius: 22px;
  }
  .card-front { top: 61px; background: var(--card-white); }
  .card-back { top: 512px; background: var(--card-navy); }

  .identity {
    position: absolute; right: 415px; top: 171px; text-align: right;
  }
  .identity-name {
    color: var(--accent-blue); font-weight: 600; font-size: 20px; line-height: 26px;
  }
  .identity-title {
    color: var(--ink-navy); font-weight: 700; font-size: 14px; line-height: 20px;
  }
  .divider {
    position: absolute; left: 288px; top: 139px; width: 1px; height: 109px;
    background: var(--rule-grey);
  }
  .contact-list {
    position: absolute; left: 307px; top: 141px; list-style: none;
  }
  .contact-item {
    display: flex; align-items: center; height: 20.4px;
    color: var(--ink-grey); font-size: 14.5px;
  }
  .contact-icon { width: 14px; height: 14px; margin-right: 11px; fill: var(--accent-blue); flex: none; }
  .address {
    position: absolute; left: 0; right: 0; top: 331px;
    display: flex; justify-content: center; align-items: center;
    color: var(--ink-grey); font-size: 14.5px;
  }
  .address .contact-icon { width: 13px; height: 17px; margin-right: 6px; }

  .brand-name {
    position: absolute; left: 0; right: 0; top: 190px;
    text-align: center; color: var(--accent-blue);
    font-weight: 300; font-size: 26px; letter-spacing: -0.3px;
  }
</style>
</head>
<body>
<div class="canvas">
  <section class="card card-front">
    <div class="identity">
      <div class="identity-name">Owen Hartley</div>
      <div class="identity-title">President</div>
    </div>
    <div class="divider"></div>
    <ul class="contact-list">
      <li class="contact-item">
        <svg class="contact-icon" viewBox="0 0 16 16"><path d="M1 5c0-2 3-3 7-3s7 1 7 3v1h-4V5H5v1H1z"/><path d="M3 7h10l1 6H2z"/><circle cx="8" cy="10" r="1.6" fill="#fff"/></svg>
        (555) 4120-3187
      </li>
      <li class="contact-item">
        <svg class="contact-icon" viewBox="0 0 16 16"><path d="M4 0h8a1 1 0 0 1 1 1v14a1 1 0 0 1-1 1H4a1 1 0 0 1-1-1V1a1 1 0 0 1 1-1zm1 2v10h6V2z"/></svg>
        (555) 2964-7710
      </li>
      <li class="contact-item">
        <svg class="contact-icon" viewBox="0 0 16 16"><path d="M4 1h7l1 1v4H4z"/><path d="M1 7h14v6H1z"/><rect x="3" y="11" width="10" height="4"/></svg>
        (555) 3081-5942
      </li>
      <li class="contact-item">
        <svg class="contact-icon" viewBox="0 0 16 16"><path d="M1 3h14v1L8 9 1 4z"/><path d="M1 6l7 5 7-5v7H1z"/></svg>
        info@brindlewoodortho.com
      </li>
      <li class="contact-item">
        <svg class="contact-icon" viewBox="0 0 16 16"><circle cx="8" cy="8" r="7"/><path d="M5 4c2 0 2 2 4 2s1 3-1 3-2 2-3 1 0-3-1-4z" fill="#fff"/></svg>
        brindlewoodortho.com
      </li>
    </ul>
    <div class="address">
      <svg class="contact-icon" viewBox="0 0 12 16"><path d="M6 0a6 6 0 0 1 6 6c0 4-6 10-6 10S0 10 0 6a6 6 0 0 1 6-6zm0 3.5a2.5 2.5 0 1 0 0 5 2.5 2.5 0 0 0 0-5z"/></svg>
      4127 Larkspur Avenue, Maple Ridge, NY 11420
    </div>
  </section>

  <section class="card card-back">
    <div class="brand-name">The Brindlewood Orthopaedic Centre</div>
  </section>
</div>
</body>
</html>
```